New audiology website PSD design only - guaranteed

We need a clean and attractive website to replace an existing Audiology (hearing technology) website which will be wordpress based.
The current website is: http://pelmorahearing.com.au
They have a new logo and colors which you can find at www.quodel.net/temp/plh2018.pdf
We will no longer have a web shop in the new website
To enter the competition, we only need a sample of the home page.
The winning design will be asked to produce 2 standard page template alternatives as well (based on the winning home page design, but for a standard page layout)
The winning design must provide any photos used
We want a clean, credible site but with some warmth
Target Market(s)
All ages but needs to include the elderly
Industry/Entity Type
Medical And Science
Number of Pages Required
3 page
Look and feel
Each slider illustrates characteristics of the customer's brand and the style your logo design should communicate.

```html
<!DOCTYPE html>
<html lang="en">
<head>
<meta charset="utf-8">
<title>Pelmora Hearing – Hearing and Balance Clinic</title>
<link href="https://fonts.googleapis.com/css2?family=Poppins:wght@400;500;600&family=Noto+Serif:ital@1&display=swap" rel="stylesheet">
<style>
:root{
  --orange:#f26f21;
  --dark:#3d3d3f;
  --ink:#2b2b2b;
  --body:#5a5a5a;
  --light:#f2f2f2;
  --line:#dedede;
  --white:#ffffff;
}
*{margin:0;padding:0;box-sizing:border-box}
html,body{width:1200px;height:2353px;overflow:hidden}
body{font-family:'Poppins',sans-serif;color:var(--body);background:var(--white);position:relative}
.abs{position:absolute}
.top-bar{left:0;top:0;width:1200px;height:34px;background:var(--orange);color:var(--white);font-size:11.5px;font-weight:500;text-align:center;line-height:34px}
.site-header{left:0;top:34px;width:1200px;height:63px;background:var(--white)}
.brand{left:172px;top:18px;display:flex;align-items:center;gap:9px;font-size:20px;font-weight:500;color:var(--ink)}
.brand-dot{width:26px;height:26px;border-radius:50%;background:var(--orange)}
.main-nav{left:424px;top:0;height:63px;display:flex;gap:0;font-size:11px;font-weight:500;color:#666}
.main-nav span{position:absolute;top:24px;white-space:nowrap}
.main-nav .active{color:var(--orange)}
.hero{left:0;top:97px;width:1200px;height:452px;background:linear-gradient(100deg,#1f2624 0%,#3b4240 40%,#556058 65%,#2c3331 100%)}
.hero-title{left:172px;top:134px;width:360px;font-size:23px;font-weight:600;line-height:30px;color:var(--white)}
.hero-title em{font-style:normal;color:var(--orange)}
.btn{background:var(--orange);color:var(--white);font-size:11.5px;font-weight:500;text-align:center}
.hero-btn{left:172px;top:275px;width:155px;height:37px;line-height:37px}
.slider-dots{left:172px;top:421px;display:flex;gap:4px}
.slider-dots i{width:9px;height:9px;border-radius:50%;background:#e8e8e8}
.slider-dots i:first-child{background:var(--orange)}
.call-bar{left:0;top:549px;width:600px;height:74px;background:var(--orange);color:var(--white);font-family:'Noto Serif',serif;font-style:italic;font-size:19px;line-height:74px;padding-left:172px}
.call-bar b{font-family:'Poppins',sans-serif;font-style:normal;font-weight:500;font-size:23px;margin-left:6px}
.call-note{left:600px;top:549px;width:600px;height:74px;background:var(--dark);color:var(--white);font-size:11.5px;line-height:17px;padding:18px 0 0 42px}
.call-arrow{left:584px;top:570px}
.services{left:0;top:623px;width:1200px;height:522px;background:var(--light)}
.eyebrow{width:1200px;left:0;text-align:center;color:var(--orange);font-size:11px}
.section-title{width:1200px;left:0;text-align:center;color:var(--ink);font-size:22px;font-weight:500}
.svc{font-size:11.5px;color:#555;white-space:nowrap}
.svc-left{right:800px;text-align:right}
.svc-right{left:798px}
.svc-rule{height:1px;background:var(--line)}
.svc-mark{width:8px;height:8px;border:1.5px solid var(--orange);border-radius:50%}
.svc-circle{left:465px;top:740px;width:270px;height:270px;border-radius:50%;background:var(--white);box-shadow:0 2px 6px rgba(0,0,0,.12)}
.svc-photo{left:475px;top:750px;width:250px;height:250px;border-radius:50%;background:radial-gradient(circle at 50% 55%,#f58a45,#f26f21 70%)}
.svc-btn{left:533px;top:1048px;width:134px;height:37px;line-height:37px}
.welcome-photo{left:659px;top:1145px;width:541px;height:433px;background:linear-gradient(90deg,#ffffff 0%,#d9dde0 30%,#9aa3aa 65%,#6f7a83 100%)}
.welcome-kicker{left:172px;top:1192px;color:var(--orange);font-size:11px}
.welcome-title{left:172px;top:1206px;color:var(--ink);font-size:23px;font-weight:500}
.welcome-copy{left:172px;top:1252px;width:490px;font-size:11.5px;line-height:21px;color:#555}
.welcome-copy p+p{margin-top:21px}
.welcome-btn{left:172px;top:1481px;width:101px;height:37px;line-height:37px}
.makers{left:0;top:1578px;width:1200px;height:411px;background:var(--dark)}
.makers-title{color:var(--white)}
.maker-grid{left:172px;top:1704px;width:856px;height:225px;background:var(--white);display:grid;grid-template-columns:repeat(4,1fr);grid-template-rows:repeat(2,1fr)}
.maker{display:flex;align-items:center;justify-content:center;font-size:26px;font-weight:500;color:#9a9a9a;border-right:1px solid #ececec;border-bottom:1px solid #ececec}
.maker:nth-child(4n){border-right:0}
.maker:nth-child(n+5){border-bottom:0}
.site-footer{left:0;top:1989px;width:1200px;height:364px;background:var(--orange);color:var(--white)}
.foot-col{top:2053px;font-size:11.5px;line-height:19.6px}
.foot-col h4{font-size:12px;font-weight:600;margin-bottom:3px}
.foot-brand{left:831px;top:2045px;display:flex;align-items:center;gap:9px;font-size:21px;font-weight:500}
.foot-dot{width:26px;height:26px;border-radius:50%;border:2px solid var(--white)}
.stay{left:831px;top:2122px;font-size:12px;font-weight:600}
.socials{left:831px;top:2150px;display:flex;gap:9px}
.socials i{width:28px;height:28px;border:1.5px solid var(--white)}
.copyright{left:0;top:2268px;width:1200px;text-align:center;font-size:11.5px;line-height:20px}
</style>
</head>
<body>

<div class="abs top-bar">Speak to Pelmora Audiologist Today! - (02) 5550 1847 &nbsp;|&nbsp; Trading Hours: Monday to Friday - 9am to 5pm</div>

<header class="abs site-header">
  <div class="abs brand"><span class="brand-dot"></span>Pelmora Hearing</div>
  <nav class="abs main-nav">
    <span class="active" style="left:0">Your Hearing</span>
    <span style="left:94px">Hearing Aids</span>
    <span style="left:186px">Musicians</span>
    <span style="left:265px">Doctors Information</span>
    <span style="left:398px">About Us</span>
    <span style="left:469px">Products</span>
    <span style="left:539px">Contact Us</span>
  </nav>
</header>

<section class="abs hero" role="img" aria-label="Close-up photo of a hearing aid being fitted behind a patient's ear"></section>
<h1 class="abs hero-title"><em>Pelmora Hearing</em> is a leading Hearing and Balance Clinic located in the inner suburbs of Sydney.</h1>
<div class="abs btn hero-btn">Appointment Today!</div>
<div class="abs slider-dots"><i></i><i></i><i></i><i></i><i></i></div>

<div class="abs call-bar">Call for an Appointment <b>(02) 5550 1847</b></div>
<div class="abs call-note">We will ensure a same-day appointment for all urgent Audiograms<br>and the earliest possible time for more complex testing.</div>
<svg class="abs call-arrow" width="18" height="32" viewBox="0 0 18 32"><path d="M18 0 L0 16 L18 32 Z" fill="#3d3d3f"/></svg>

<section class="abs services"></section>
<div class="abs eyebrow" style="top:679px">Pelmora Hearing's Diagnostic</div>
<h2 class="abs section-title" style="top:694px">Services We Offer</h2>

<div class="abs svc svc-left" style="top:801px">Adult Hearing Test</div>
<div class="abs svc svc-left" style="top:837px">Paediatric Hearing Test</div>
<div class="abs svc svc-left" style="top:874px">Auditory Brainstem Response</div>
<div class="abs svc svc-left" style="top:910px">VideoNystagmography (VNG)</div>
<div class="abs svc svc-left" style="top:946px">Caloric Testing</div>
<div class="abs svc-mark" style="left:412px;top:805px"></div>
<div class="abs svc-mark" style="left:412px;top:841px"></div>
<div class="abs svc-mark" style="left:412px;top:878px"></div>
<div class="abs svc-mark" style="left:412px;top:914px"></div>
<div class="abs svc-mark" style="left:412px;top:950px"></div>
<div class="abs svc-rule" style="left:172px;top:828px;width:250px"></div>
<div class="abs svc-rule" style="left:172px;top:864px;width:250px"></div>
<div class="abs svc-rule" style="left:172px;top:901px;width:250px"></div>
<div class="abs svc-rule" style="left:172px;top:937px;width:250px"></div>

<div class="abs svc svc-right" style="top:803px">Cortical Evoked Response Audiometry</div>
<div class="abs svc svc-right" style="top:839px">Auditory Steady State Response</div>
<div class="abs svc svc-right" style="top:875px">Vestibular Evoked Myogenic Potentials</div>
<div class="abs svc svc-right" style="top:911px">Electrocochleography</div>
<div class="abs svc svc-right" style="top:947px">Tinnitus</div>
<div class="abs svc-mark" style="left:779px;top:807px"></div>
<div class="abs svc-mark" style="left:779px;top:843px"></div>
<div class="abs svc-mark" style="left:779px;top:879px"></div>
<div class="abs svc-mark" style="left:779px;top:915px"></div>
<div class="abs svc-mark" style="left:779px;top:951px"></div>
<div class="abs svc-rule" style="left:779px;top:830px;width:250px"></div>
<div class="abs svc-rule" style="left:779px;top:866px;width:250px"></div>
<div class="abs svc-rule" style="left:779px;top:902px;width:250px"></div>
<div class="abs svc-rule" style="left:779px;top:938px;width:250px"></div>

<div class="abs svc-circle"></div>
<div class="abs svc-photo" role="img" aria-label="Hand holding a small behind-the-ear hearing aid on an orange background"></div>
<div class="abs btn svc-btn">View All Services</div>

<div class="abs welcome-photo" role="img" aria-label="Photo of an audiologist chatting with an older patient"></div>
<div class="abs welcome-kicker">Welcome</div>
<h2 class="abs welcome-title">Pelmora Hearing</h2>
<div class="abs welcome-copy">
  <p>Pelmora Hearing is an independently owned and managed professional audiology clinic. Our Audiologists are health-care professionals specialising in diagnosing, treating and monitoring everything to do with hearing and balance. At Pelmora Hearing we work closely with Ear, Nose and Throat specialists to ensure you receive the highest standards of medical care.</p>
  <p>Pelmora Hearing are state of the art hearing and balance clinics. We provide all brands of digital hearing aids, cochlear implants and assisted listening devices. We are diagnostic clinics, offering hearing tests for adults and children, balance tests, tinnitus testing and treatment, and auditory processing tests (APD).</p>
</div>
<div class="abs btn welcome-btn">Learn More</div>

<section class="abs makers"></section>
<div class="abs eyebrow" style="top:1634px">Our</div>
<h2 class="abs section-title makers-title" style="top:1650px">Manufacturers</h2>
<div class="abs maker-grid">
  <div class="maker">Aurelle</div>
  <div class="maker">Brevan</div>
  <div class="maker">Calyx</div>
  <div class="maker">Dorvel</div>
  <div class="maker">Elmari</div>
  <div class="maker">Fennick</div>
  <div class="maker">Gravane</div>
  <div class="maker">Holtbury</div>
</div>

<footer class="abs site-footer"></footer>
<div class="abs foot-col" style="left:172px;color:var(--white)">
  <h4>Contact Info</h4>
  Wren Hill<br>Ground Floor, Suite 4,<br>18 Larkspur Road,<br>Wren Hill, NSW, 2071<br><br>Ph: 5550 1847<br>Email us
</div>
<div class="abs foot-col" style="left:392px;top:2073px;color:var(--white)">
  Corran Bay<br>Shop 2, 40 Tilbury<br>Parade, Corran Bay,<br>NSW, 2049<br><br>Ph: 5550 2936<br>Email us
</div>
<div class="abs foot-col" style="left:610px;color:var(--white)">
  <h4>Quick Links</h4>
  Your Hearing<br>Hearing Aids<br>Musicians<br>Doctors Information<br>About Us<br>Products<br>Contact Us
</div>
<div class="abs foot-brand" style="color:var(--white)"><span class="foot-dot"></span>Pelmora Hearing</div>
<div class="abs stay" style="color:var(--white)">Stay Connected</div>
<div class="abs socials"><i></i><i></i><i></i></div>
<div class="abs copyright" style="color:var(--white)">Copyright © Pelmora Hearing. All Rights Reserved<br>Terms and Conditions</div>

</body>
</html>
```